Bellmoor Commercial Finance Information Brochure

This brochure will be sent out to clients via A4 PDF on an email to showcase what our company has to offer. We are a commercial finance brokerage, that specialises in property finance. We would like to see designs following our colour scheme. The final design should demonstrate our professionalism and reliability.
I have attached our logo and also a few bullet points on our information and what we can offer. These can be slightly reworded for conciseness. Or leave the text sections as filler and I can fill these in.
I have also attached an overview of our colour scheme and design styling for your consideration.
Target Market(s)
Property Developers
Industry/Entity Type
Financial Services

```html
<!DOCTYPE html>
<html lang="en">
<head>
<meta charset="utf-8">
<title>Bellmoor Finance – Information Brochure</title>
<link href="https://fonts.googleapis.com/css2?family=Figtree:wght@400;500;600;700&display=swap" rel="stylesheet">
<style>
  :root {
    --brand-blue: #0751a3;
    --brand-green: #25893f;
    --ink: #2e2e2e;
    --paper: #ffffff;
    --backdrop: #e6e7e9;
  }
  * { margin: 0; padding: 0; box-sizing: border-box; }
  html, body {
    width: 1200px; height: 1200px; overflow: hidden;
    background: var(--backdrop);
    font-family: "Figtree", "Helvetica Neue", Arial, sans-serif;
  }
  .sheet {
    position: absolute; left: 190px; top: 42px;
    width: 820px; height: 1116px;
    background: var(--paper);
    overflow: hidden;
    box-shadow: 0 6px 24px rgba(0,0,0,0.18);
  }
  .top-rule {
    position: absolute; left: 0; top: 0; width: 820px; height: 10px;
    background: var(--brand-blue);
  }
  .top-rule::after {
    content: ""; position: absolute; right: 0; top: 10px;
    width: 240px; height: 4px; background: var(--brand-green);
  }
  .brand-name {
    position: absolute; left: 82px; top: 86px;
    font-size: 34px; font-weight: 700; letter-spacing: 1px;
    color: var(--brand-blue); text-transform: uppercase; line-height: 1.1;
  }
  .body-copy {
    position: absolute; left: 82px; top: 218px; width: 654px;
    color: var(--ink); font-size: 15.2px; line-height: 19.9px;
    letter-spacing: 0.65px; text-align: justify;
  }
  .body-copy p + p { margin-top: 19.8px; }
  .body-copy p:first-child { text-indent: 22px; }
  .brand-mention { color: var(--brand-blue); }
  .footer-accent {
    position: absolute; left: 0; top: 1004px; width: 820px; height: 6px;
    background: var(--brand-green);
  }
  .footer-band {
    position: absolute; left: 0; top: 1018px; width: 820px; height: 98px;
    background: var(--brand-blue);
  }
  .contact-list {
    position: absolute; left: 32px; top: 1034px;
    list-style: none; color: #fff; font-size: 12.3px; font-weight: 500; line-height: 16px;
  }
  .contact-list li { display: flex; align-items: center; gap: 6px; }
  .contact-list svg { width: 11px; height: 11px; flex: none; }
  .office-address {
    position: absolute; right: 89px; top: 1081px;
    color: #fff; font-size: 13.8px; font-weight: 500;
    display: flex; align-items: center; gap: 5px;
  }
  .office-address svg { width: 11px; height: 14px; }
</style>
</head>
<body>
<main class="sheet">
  <div class="top-rule" aria-hidden="true"></div>

  <div class="brand-name">Bellmoor Finance</div>

  <section class="body-copy">
    <p>As former lenders and developers ourselves, we intimately understand the inefficiencies that plague deals in the market today. We’ve experienced the frustration of tight time limits on deals and the exasperating feeling of brokers wasting precious time collecting information. It’s enough to drive developers and lenders insane!</p>
    <p>That’s why we founded <span class="brand-mention">Bellmoor Finance</span> – to be the efficient and reliable link that connects developers and lenders. We’ve streamlined our processes to eliminate unnecessary hurdles, enabling clear and swift communication between all parties involved. No more wasted time. No more unnecessary stress.</p>
    <p>With our expertise and industry insights, we’ve developed a unique approach that simplifies the financing journey. From the initial consultation to the final funding, we’re here to guide you every step of the way. Our goal? To make commercial financing a smooth and enjoyable experience for you.</p>
    <p>With our background in the asset management industry, we have cultivated a black book of fund managers, institutions, UHNWI and private equity lenders that we can call on for non-traditional lending.</p>
    <p><span class="brand-mention">Bellmoor Finance</span> was created to satisfy a need in the market that has been far too overlooked. Efficiency. Efficiency is at the heart of our operations, and we pride ourselves on our ability to secure the best financing options swiftly and effectively for our clients. By employing cutting-edge technology and streamlining our internal processes, we have cultivated a seamless and time-saving approach to finance brokering. Having been a developer, we understand the stresses and headaches associated with building, let alone all the paperwork and emails backwards and forwards between yourself and brokers to attain the necessary financing.</p>
    <p>We are well-versed in the questions lenders will ask, allowing us to get ahead of the curve and request all the necessary information from you on day one. This approach provides you with a distinct advantage, as it eliminates the need to allocate hours each day to answering questions and fulfilling requests from brokers. By entrusting us with this responsibility, you can focus on your core tasks and leave the financing aspect to us, making the process less stressful for you.</p>
  </section>

  <div class="footer-accent" aria-hidden="true"></div>
  <div class="footer-band" aria-hidden="true"></div>

  <ul class="contact-list">
    <li><svg viewBox="0 0 12 12"><path d="M2.5 1 L4.5 3.2 L3.6 4.6 Q5 7 7.4 8.4 L8.8 7.5 L11 9.5 L9.6 11 Q4.5 10.5 1 2.4 Z" fill="#fff"/></svg>555-204-7781</li>
    <li><svg viewBox="0 0 12 12"><rect x="3" y="0.5" width="6" height="11" rx="1" fill="none" stroke="#fff" stroke-width="1.3"/><circle cx="6" cy="9.6" r="0.7" fill="#fff"/></svg>555-318-6620</li>
    <li><svg viewBox="0 0 12 12"><rect x="0.5" y="2.5" width="11" height="7.5" fill="#fff"/><path d="M0.5 2.5 L6 7 L11.5 2.5" fill="none" stroke="#0751a3" stroke-width="1"/></svg>info@bellmoorfinance.com</li>
    <li><svg viewBox="0 0 12 12"><circle cx="6" cy="6" r="5.3" fill="none" stroke="#fff" stroke-width="1.2"/><path d="M0.7 6 H11.3 M6 0.7 Q2.5 6 6 11.3 M6 0.7 Q9.5 6 6 11.3" fill="none" stroke="#fff" stroke-width="1"/></svg>www.bellmoorfinance.com</li>
  </ul>

  <div class="office-address">
    <svg viewBox="0 0 11 14"><path d="M5.5 0.8 A4.5 4.5 0 0 1 10 5.3 C10 8.5 5.5 13.2 5.5 13.2 C5.5 13.2 1 8.5 1 5.3 A4.5 4.5 0 0 1 5.5 0.8 Z" fill="none" stroke="#fff" stroke-width="1.4"/><circle cx="5.5" cy="5.3" r="1.6" fill="#fff"/></svg>
    4120 Harbor View Road Juneau, Alaska 99801
  </div>
</main>
</body>
</html>
```